Korelith InsurTech Website Redesign - 10 Pages

Design a modern, professional website for Korelith, an AI-native cyber insurance platform serving SMBs.

DELIVERABLE: 10 pages (desktop + mobile mockups)
- Homepage (priority #1)
- 4 Platform pages (Cyber Insurance, Brokers, Underwriters, Policyholder)
- 3 Company pages (About Us, Team, Contact/Careers)
- 2 Risk pages (AI Risk, Cyber Risk)

DESIGN DIRECTION:
- Professional + innovative (insurance meets technology)
- Trust-building + modern aesthetic
- Reference: Brambury Insurance, Tidewick Insurance
- Use official brand colors (6-color palette provided)
- Avoid generic security clipart (padlocks, shields, magnifying glasses)
- Custom graphics, not AI-generated or stock imagery

CURRENT SITES FOR REFERENCE:
- www.korelith.ai
- https://a3c9124d.korelith-website.vorlapages.dev/

Full detailed brief with all content, page specifications, and brand guidelines attached as PDF (Korelith_PixelHarbor_Brief.pdf).

TARGET AUDIENCE: Insurance brokers (primary), SMB business owners (secondary)
KEY MESSAGE: "Cyber Insurance the Way It Should Be"

Additional brand assets available in Google Drive - link provided on request.

```html
<!DOCTYPE html>
<html lang="en">
<head>
<meta charset="utf-8">
<title>Korelith — Cyber Insurance the Way It Should Be</title>
<link href="https://fonts.googleapis.com/css2?family=Montserrat:wght@500;600;700&family=Inter:wght@400;500;600&display=swap" rel="stylesheet">
<style>
:root{
  --navy:#18235a;
  --navy-deep:#111a47;
  --card:#1f2c66;
  --green:#8ef59a;
  --teal:#5ec9bf;
  --blue:#3b3ff0;
  --white:#ffffff;
  --ink:#14204f;
  --muted:#c9d0ea;
  --faint:#22306f;
  --head:'Montserrat',sans-serif;
  --body:'Inter',sans-serif;
}
*{box-sizing:border-box;margin:0;padding:0}
html,body{width:1200px;height:3778px;overflow:hidden}
body{background:var(--navy);color:var(--white);font-family:var(--body);position:relative}
.abs{position:absolute}
h2.section-title{position:absolute;left:0;width:1200px;text-align:center;font-family:var(--head);font-weight:600;font-size:32px}
p.section-sub{position:absolute;left:0;width:1200px;text-align:center;font-size:11.5px;line-height:16px;color:var(--muted)}

/* Hero */
.hero{position:absolute;top:0;left:0;width:1200px;height:641px;background:radial-gradient(ellipse at 55% 0%,#2f7a69 0%,#1c3d5f 35%,var(--navy-deep) 75%);overflow:hidden}
.brand{position:absolute;display:flex;align-items:center;gap:8px;font-family:var(--head);font-weight:700;color:var(--teal)}
.brand .dot{width:14px;height:14px;border-radius:50%;background:var(--teal)}
.nav{position:absolute;top:20px;left:690px;display:flex;align-items:center;gap:32px;font-size:12.5px}
.nav .demo{border:1px solid #cfd6ee;border-radius:3px;padding:10px 14px;display:flex;gap:18px;align-items:center}
.hero h1{position:absolute;left:108px;top:178px;font-family:var(--head);line-height:1}
.hero h1 .l1{display:block;font-size:118px;font-weight:600;color:var(--teal);letter-spacing:1px}
.hero h1 .l2{display:block;font-size:66px;font-weight:600;margin-top:6px}
.hero h1 .l3{display:block;font-size:35px;font-weight:600;margin-top:8px}
.hero .lead{position:absolute;left:111px;top:422px;font-size:12px}
.btn{display:flex;align-items:center;justify-content:space-between;gap:14px;font-size:12.5px;font-weight:500;color:var(--ink)}
.btn-green{background:var(--green)}
.hero .btn{position:absolute;left:113px;top:461px;width:123px;height:39px;padding:0 14px}
.hero-art{position:absolute;left:560px;top:90px;width:640px;height:551px;background:radial-gradient(ellipse at 55% 60%,#2a5f95 0%,#1f3f7c 40%,rgba(24,35,90,0) 75%)}

/* Marquee */
.marquee{position:absolute;left:0;width:1200px;height:33px;background:var(--green);color:#141d48;overflow:hidden;display:flex;align-items:center;white-space:nowrap;font-family:var(--head);font-weight:500;font-size:18px}
.marquee span{display:inline-flex;align-items:center;gap:70px;margin-right:70px}
.marquee svg{width:12px;height:12px}

/* Different */
.hub{position:absolute;width:74px;height:74px;border-radius:50%;background:#fff;border:3px solid #c9b896;display:flex;align-items:center;justify-content:center;font-family:var(--head);font-weight:700;font-size:11px;color:#2d3a6a}
.features{position:absolute;top:932px;left:113px;display:flex;gap:13px}
.feature{width:184px;height:212px;background:var(--card);border-bottom:3px solid #3a4a8c;border-radius:4px;text-align:center;padding:30px 10px 0}
.feature svg{width:34px;height:34px;margin-bottom:18px}
.feature h3{font-size:13.5px;font-weight:500;line-height:17px;margin-bottom:5px}
.feature p{font-size:10px;line-height:15px;color:var(--muted)}

/* Tools */
.tools-band{position:absolute;top:1198px;left:0;width:1200px;height:410px;background:linear-gradient(180deg,#1a2763,#1c2b6a 70%,var(--navy))}
.dash{position:absolute;top:1247px;left:113px;width:491px;height:337px;border:1px solid #8e97bf;border-radius:3px;padding:10px;background:#1d2a63}
.tools-panel{position:absolute;top:1247px;left:640px;width:444px;height:337px;background:var(--teal);border-radius:4px;padding:40px 44px}
.tools-panel h2{font-family:var(--head);font-weight:500;font-size:32px;line-height:38px}
.tools-panel p{font-size:11px;line-height:16px;margin:14px 0 14px;color:#eaf8f5}
.tools-panel li{list-style:none;font-size:11.5px;display:flex;align-items:center;gap:10px;height:24.5px}
.tools-panel li::before{content:"";border-left:9px solid var(--ink);border-top:6px solid transparent;border-bottom:6px solid transparent}
.watermark{position:absolute;left:0;width:1200px;text-align:center;font-family:var(--head);font-weight:600;font-size:118px;line-height:1;color:var(--faint);white-space:nowrap;letter-spacing:1px}

/* DNA */
.dna{position:absolute;top:1841px;left:113px;display:flex}
.dna-item{width:242px;height:242px;position:relative;display:flex;align-items:center;justify-content:center}
.dna-item .ring{position:absolute;inset:0;border-radius:50%;border:1.5px solid #b7a277;clip-path:polygon(0 0,100% 0,100% 100%,0 60%)}
.dna-item .disc{width:222px;height:222px;border-radius:50%;background:radial-gradient(circle at 50% 100%,#3a8a78 0%,#1e3a6a 45%,#19265e 70%);display:flex;flex-direction:column;align-items:center;justify-content:center;text-align:center;font-size:14.5px;font-weight:500;line-height:19px;padding:0 22px}
.dna-item svg{width:50px;height:50px;margin-bottom:18px}

/* Lifecycle */
.stages{position:absolute;left:223px;top:2288px;width:754px;height:400px}
.stage-text{position:absolute;width:140px;font-size:10.2px;line-height:15.5px}
.stage-text b{display:flex;align-items:center;gap:5px;font-size:15px;font-weight:600;margin-bottom:2px}
.stage-text b::after{content:"";border-left:8px solid currentColor;border-top:6px solid transparent;border-bottom:6px solid transparent}

/* Integrations */
.tabs{position:absolute;top:2795px;left:264px;display:flex;gap:6px}
.tab{height:39px;padding:0 25px;display:flex;align-items:center;font-size:13px;background:#1d2a66}
.tab.active{background:var(--green);color:var(--ink)}
.logos{position:absolute;top:2959px;left:265px;display:flex;gap:13px}
.logo-box{width:213px;height:93px;background:#fff;display:flex;align-items:center;justify-content:center;gap:8px;font-weight:500;font-size:22px;color:#3a3f55}
.logo-box i{width:14px;height:14px;background:#5c6275;border-radius:50%;display:block}

/* CTA */
.cta{position:absolute;top:3232px;left:113px;width:974px;height:292px;background:linear-gradient(110deg,#1e9b8f,#5ec9bf 45%,#6fd3c4);overflow:hidden}
.cta h2{position:absolute;left:60px;top:80px;font-family:var(--head);font-weight:500;font-size:32px}
.cta p{position:absolute;left:60px;top:126px;width:390px;font-size:11px;line-height:16px}
.cta .btn{position:absolute;left:57px;top:182px;width:124px;height:40px;padding:0 14px;background:#fff}
.cta-photo{position:absolute;left:630px;top:3140px;width:400px;height:384px;border-radius:200px 200px 0 0;background:linear-gradient(180deg,#7a5a45,#6a8aa8 45%,#3e5d80)}

/* Footer */
.footer{position:absolute;top:3557px;left:0;width:1200px;height:221px}
.footer .about{position:absolute;left:113px;top:110px;font-size:9.5px;line-height:14px;color:var(--muted);width:190px}
.footer .divider{position:absolute;left:317px;top:0;width:1px;height:130px;background:#3a4680}
.fcol{position:absolute;top:0}
.fcol h4{font-family:var(--head);font-weight:500;font-size:15px;margin-bottom:10px}
.fcol .link{display:flex;align-items:center;gap:8px;color:var(--muted);font-size:10px;height:20px}
.fcol.social .link{height:35px}
.fcol.social .link i{width:20px;height:20px;border-radius:50%;background:#2e4ad0;display:block}
.news p{font-size:9.5px;color:var(--muted);line-height:12px;margin-bottom:10px;width:140px}
.news .field{width:164px;height:40px;background:#1d2a66;font-size:9.5px;color:var(--muted);display:flex;align-items:center;padding-left:14px}
.news .btn{width:126px;height:34px;padding:0 14px;margin-top:10px}
.copyright{position:absolute;top:3753px;left:0;width:1200px;text-align:center;font-size:9px;color:var(--muted)}
</style>
</head>
<body>

<header class="hero">
  <div class="hero-art" role="img" aria-label="Hero artwork: cyber analyst working at glowing monitors"></div>
  <div class="brand" style="left:113px;top:34px;font-size:20px"><span class="dot"></span>korelith</div>
  <nav class="nav">
    <span>Platform ⌄</span><span>Resources</span><span>Company ⌄</span>
    <span class="demo">Get a Demo
      <svg width="10" height="12" viewBox="0 0 10 12"><path d="M0 0L10 6L0 12Z" fill="#fff"/></svg></span>
  </nav>
  <h1><span class="l1">Cyber</span><span class="l2">Insurance</span><span class="l3">the Way It Should Be</span></h1>
  <p class="lead">Evidence based, automation driven underwriting for the AI era</p>
  <div class="btn btn-green">Contact Us <svg width="10" height="12" viewBox="0 0 10 12"><path d="M0 0L10 6L0 12Z" fill="#14204f"/></svg></div>
</header>

<div class="marquee" style="top:642px">
  <span style="margin-left:-30px">relith <svg viewBox="0 0 10 12"><path d="M0 0L10 6L0 12Z" fill="#141d48"/></svg></span>
  <span>Korelith <svg viewBox="0 0 10 12"><path d="M0 0L10 6L0 12Z" fill="#141d48"/></svg></span>
  <span>Korelith <svg viewBox="0 0 10 12"><path d="M0 0L10 6L0 12Z" fill="#141d48"/></svg></span>
  <span>Korelith <svg viewBox="0 0 10 12"><path d="M0 0L10 6L0 12Z" fill="#141d48"/></svg></span>
  <span>Korelith <svg viewBox="0 0 10 12"><path d="M0 0L10 6L0 12Z" fill="#141d48"/></svg></span>
  <span>Korelith</span>
</div>

<h2 class="section-title" style="top:724px">What Makes Korelith Different</h2>
<p class="section-sub" style="top:768px">The Korelith platform streamlines the entire policy lifecycle, incentivizes and empowers<br>policyholders to actively reduce their risk, and elevates brokers as trusted advisors.</p>
<svg class="abs" style="left:0;top:860px" width="1200" height="75" viewBox="0 0 1200 75">
  <g fill="none" stroke="#6a76a8" stroke-width="1">
    <path d="M205 72V12H562M995 72V12H638M403 72V30H562M797 72V30H638M600 50V72"/>
  </g>
  <g fill="#8c97c4"><circle cx="205" cy="72" r="3"/><circle cx="403" cy="72" r="3"/><circle cx="600" cy="72" r="3"/><circle cx="797" cy="72" r="3"/><circle cx="995" cy="72" r="3"/></g>
</svg>
<div class="hub" style="left:563px;top:836px">korelith</div>
<div class="features">
  <div class="feature">
    <svg viewBox="0 0 34 34"><rect x="6" y="6" width="22" height="26" rx="4" fill="var(--blue)"/><rect x="12" y="2" width="10" height="7" rx="2" fill="var(--blue)"/><circle cx="17" cy="20" r="6" fill="var(--green)"/></svg>
    <h3>Platform<br>driven Assessment</h3>
    <p>Standardized, repeatable cyber risk evaluations embedded directly into the insurance workflow.</p>
  </div>
  <div class="feature">
    <svg viewBox="0 0 34 34"><path d="M15 4A14 14 0 1 0 30 19H15Z" fill="var(--blue)"/><path d="M19 0A14 14 0 0 1 33 15H19Z" fill="var(--green)"/></svg>
    <h3>Automated Analysis<br>of Cyber Risk Data</h3>
    <p>Continuous ingestion and analysis of complex cyber risk data—without manual overhead.</p>
  </div>
  <div class="feature">
    <svg viewBox="0 0 34 34"><circle cx="17" cy="17" r="15" fill="var(--blue)"/><circle cx="17" cy="17" r="9" fill="var(--card)"/><rect x="12" y="13" width="3" height="9" fill="var(--green)"/><rect x="17" y="10" width="3" height="12" fill="var(--green)"/></svg>
    <h3>Inside-Out &amp; Outside<br>In Data Integrations</h3>
    <p>Combines internal security telemetry with external threat intelligence and third-party data sources.</p>
  </div>
  <div class="feature">
    <svg viewBox="0 0 34 34"><circle cx="17" cy="15" r="12" fill="var(--blue)"/><circle cx="17" cy="15" r="7" fill="var(--card)"/><rect x="8" y="27" width="18" height="4" rx="2" fill="var(--blue)"/><rect x="12" y="13" width="10" height="4" fill="var(--green)"/></svg>
    <h3>AI Analysis for<br>Risk Prediction</h3>
    <p>Advanced models surface emerging threats, predict loss scenarios, and support smarter underwriting decisions.</p>
  </div>
  <div class="feature">
    <svg viewBox="0 0 34 34"><rect x="2" y="6" width="30" height="20" rx="3" fill="var(--blue)"/><rect x="12" y="28" width="10" height="4" fill="var(--blue)"/><circle cx="17" cy="8" r="6" fill="var(--green)"/></svg>
    <h3>Continuous Risk<br>Monitoring</h3>
    <p>Real-time visibility into risk posture across the policy lifecycle before, during, and after coverage.</p>
  </div>
</div>

<div class="tools-band"></div>
<div class="dash">
  <div role="img" aria-label="Dashboard screen showing a security command center with coverage, premium and risk score widgets" style="width:100%;height:100%;background:linear-gradient(90deg,#eef1f6 0 14%,#ffffff 14% 100%);position:relative">
    <svg width="469" height="315" viewBox="0 0 469 315" style="position:absolute;inset:0">
      <rect x="78" y="70" width="110" height="38" rx="3" fill="#5ec9bf" opacity=".7"/>
      <rect x="198" y="70" width="110" height="38" rx="3" fill="#5ec9bf" opacity=".7"/>
      <rect x="318" y="70" width="151" height="38" rx="3" fill="#5ec9bf" opacity=".4"/>
      <rect x="78" y="120" width="165" height="88" rx="4" fill="#eef0ff"/>
      <rect x="252" y="120" width="165" height="88" rx="4" fill="#eafaf0"/>
      <rect x="78" y="220" width="165" height="76" rx="4" fill="#fdf0ec"/>
      <rect x="252" y="220" width="165" height="76" rx="4" fill="#eaf8f6"/>
      <rect x="6" y="190" width="56" height="8" rx="2" fill="#1b3b3a"/>
    </svg>
  </div>
</div>
<div class="tools-panel">
  <h2>Proprietary Tools<br>and Rapid Response</h2>
  <p>Advanced security tools and 24/7 incident response capabilities protect businesses before, during, and after cyber events.</p>
  <ul>
    <li>In-house ransomware response &amp; system restoration</li>
    <li>Mix of in-house and verified expert contractors</li>
    <li>24/7 claims hotline with expert cyber triage</li>
    <li>US-only on-site and remote support</li>
    <li>Real-time incident tracking</li>
  </ul>
</div>
<div class="watermark" style="top:1608px">Korelith InsurTech</div>

<h2 class="section-title" style="top:1748px">Insurance DNA and Tech Execution</h2>
<p class="section-sub" style="top:1790px">Founded by a team with deep expertise in cyber insurance and cybersecurity, we understand both the risk landscape and the insurance market.</p>
<div class="dna">
  <div class="dna-item"><span class="ring"></span><div class="disc">
    <svg viewBox="0 0 50 50"><rect x="8" y="4" width="28" height="38" rx="3" fill="#fff"/><g stroke="#1a2456" stroke-width="2.5"><path d="M14 14h16M14 21h16M14 28h10"/></g><circle cx="37" cy="37" r="8" fill="var(--green)"/></svg>
    20+ years Combined insurance Experience</div></div>
  <div class="dna-item"><span class="ring"></span><div class="disc">
    <svg viewBox="0 0 50 50"><circle cx="22" cy="14" r="9" fill="#fff"/><path d="M4 44c0-12 8-18 18-18s18 6 18 18Z" fill="#fff"/><path d="M37 26l3 6 6 1-4 4 1 6-6-3-6 3 1-6-4-4 6-1Z" fill="var(--green)"/></svg>
    Cybersecurity expertise from industry leaders</div></div>
  <div class="dna-item"><span class="ring"></span><div class="disc">
    <svg viewBox="0 0 50 50"><circle cx="25" cy="12" r="9" fill="#fff"/><path d="M6 46c0-14 8-20 19-20s19 6 19 20Z" fill="#fff"/><path d="M25 26l-4 4 4 14 4-14Z" fill="var(--green)"/></svg>
    Former executives from Emberwatch, Corvane, Halden Re</div></div>
  <div class="dna-item"><span class="ring"></span><div class="disc">
    <svg viewBox="0 0 50 50"><path d="M25 2a16 16 0 0 1 16 16c0 12-16 30-16 30S9 30 9 18A16 16 0 0 1 25 2Z" fill="#fff"/><circle cx="25" cy="18" r="8" fill="var(--green)"/><circle cx="25" cy="18" r="4" fill="#1a2456"/></svg>
    Built to address first-wave InsurTech shortcomings</div></div>
</div>

<div class="marquee" style="top:2162px">
  <span style="margin-left:-16px">relith <svg viewBox="0 0 10 12"><path d="M0 0L10 6L0 12Z" fill="#141d48"/></svg></span>
  <span>Korelith <svg viewBox="0 0 10 12"><path d="M0 0L10 6L0 12Z" fill="#141d48"/></svg></span>
  <span>Korelith <svg viewBox="0 0 10 12"><path d="M0 0L10 6L0 12Z" fill="#141d48"/></svg></span>
  <span>Korelith <svg viewBox="0 0 10 12"><path d="M0 0L10 6L0 12Z" fill="#141d48"/></svg></span>
  <span>Korelith <svg viewBox="0 0 10 12"><path d="M0 0L10 6L0 12Z" fill="#141d48"/></svg></span>
  <span>Korelith</span>
</div>

<h2 class="section-title" style="top:2238px">The Complete Cyber Insurance Lifecycle</h2>
<div class="stages">
  <svg width="754" height="400" viewBox="0 0 754 400">
    <defs>
      <linearGradient id="s1" x1="0" y1="0" x2="0" y2="1"><stop offset="0" stop-color="#5fd1b8"/><stop offset="1" stop-color="#3a8f82"/></linearGradient>
      <linearGradient id="s2" x1="0" y1="0" x2="0" y2="1"><stop offset="0" stop-color="#ddd0bf"/><stop offset="1" stop-color="#c8b69c"/></linearGradient>
      <linearGradient id="s3" x1="0" y1="0" x2="0" y2="1"><stop offset="0" stop-color="#3a2cf5"/><stop offset="1" stop-color="#2b2fb0"/></linearGradient>
      <linearGradient id="s4" x1="0" y1="0" x2="0" y2="1"><stop offset="0" stop-color="#1c4f3e"/><stop offset="1" stop-color="#3e8a6c"/></linearGradient>
      <linearGradient id="s5" x1="0" y1="0" x2="0" y2="1"><stop offset="0" stop-color="#9a8560"/><stop offset="1" stop-color="#7c6a48"/></linearGradient>
    </defs>
    <path d="M0 158L73 118L146 158V400H0Z" fill="url(#s1)"/>
    <path d="M152 132L225 92L298 132V400H152Z" fill="url(#s2)"/>
    <path d="M304 99L377 59L450 99V400H304Z" fill="url(#s3)"/>
    <path d="M456 70L529 30L602 70V400H456Z" fill="url(#s4)"/>
    <path d="M608 40L681 0L754 40V400H608Z" fill="url(#s5)"/>
    <g fill="#fff" stroke-width="6">
      <circle cx="73" cy="213" r="34" stroke="#48b09c"/><circle cx="225" cy="213" r="34" stroke="#d5c6b0"/><circle cx="377" cy="213" r="34" stroke="#3430d8"/><circle cx="529" cy="213" r="34" stroke="#27604c"/><circle cx="681" cy="213" r="34" stroke="#8f7b58"/>
    </g>
    <g font-family="Montserrat,sans-serif" font-size="46" font-weight="500" text-anchor="middle" fill="none" stroke-width="1.6">
      <text x="73" y="229" stroke="#48b09c">1</text><text x="225" y="229" stroke="#c8b69c">2</text><text x="377" y="229" stroke="#3430d8">3</text><text x="529" y="229" stroke="#27604c">4</text><text x="681" y="229" stroke="#8f7b58">5</text>
    </g>
  </svg>
  <div class="stage-text" style="left:12px;top:294px"><b>Ensure</b>Best in class cyber insurance coverage with comprehensive first and third party protections</div>
  <div class="stage-text" style="left:164px;top:294px;color:#fff7ea"><b>Assess</b>Dynamic scanning and read-only API integrations to continuously evaluate risk posture and inform underwriting</div>
  <div class="stage-text" style="left:316px;top:294px"><b>Improve</b>Incentivize and guide policyholders to actively strengthen their cybersecurity through behavior rewards</div>
  <div class="stage-text" style="left:468px;top:294px"><b>Remediate</b>Expert post-breach services including forensics, restoration, and crisis management support</div>
  <div class="stage-text" style="left:620px;top:294px"><b>Renew</b>Seamless policy renewals with transparent pricing based on demonstrated risk improvements</div>
</div>

<h2 class="section-title" style="top:2737px">Seamlessly Integrates With Your Tech Stack</h2>
<div class="tabs">
  <div class="tab active">Identity Platforms</div><div class="tab">Endpoint Security</div><div class="tab">Developer Platforms</div><div class="tab">Cloud Infrastructure</div>
</div>
<svg class="abs" style="left:0;top:2900px" width="1200" height="60" viewBox="0 0 1200 60">
  <path d="M371 58V18H563M637 18H824V58" fill="none" stroke="#6a76a8"/>
</svg>
<div class="hub" style="left:563px;top:2856px">korelith</div>
<div class="logos">
  <div class="logo-box"><i></i>Orbitly Suite</div>
  <div class="logo-box"><i></i>Keyvale</div>
  <div class="logo-box" style="font-size:18px"><i></i>Stratus Directory</div>
</div>
<div class="watermark" style="top:3074px">Korelith InsurTech</div>

<section class="cta">
  <h2>Let's Secure Your Future.</h2>
  <p>We're here to help you navigate your security needs with confidence. Whether you have a question or need more information, our team is ready to assist. Fill out the form below, and we'll get back to you promptly.</p>
  <div class="btn">Get started <svg width="10" height="12" viewBox="0 0 10 12"><path d="M0 0L10 6L0 12Z" fill="#14204f"/></svg></div>
</section>
<div class="cta-photo" role="img" aria-label="Smiling advisor in a denim shirt pointing at a tablet showing a risk assessment"></div>

<footer class="footer">
  <div class="brand" style="left:113px;top:40px;font-size:18px"><span class="dot"></span>korelith</div>
  <p class="about">Reducing the frequency and severity of cyber risk by strengthening organizations' cyber risk posture.</p>
  <span class="divider"></span>
  <div class="fcol" style="left:370px"><h4>Solutions</h4><div class="link">For Carriers</div><div class="link">For Brokers</div><div class="link">For Enterprises</div></div>
  <div class="fcol" style="left:551px"><h4>Main Links</h4><div class="link">Platform</div><div class="link">Resources</div><div class="link">Company</div></div>
  <div class="fcol social" style="left:725px"><h4>Follow Us</h4><div class="link"><i></i>Friendwall</div><div class="link"><i></i>ProLinkd</div><div class="link"><i></i>Snapgrid</div></div>
  <div class="fcol news" style="left:918px"><h4>Subscribe Newsletter</h4>
    <p>Enter your email to receive 5% coupon immediately</p>
    <div class="field">Enter Your Email</div>
    <div class="btn btn-green">Subscribe <svg width="10" height="12" viewBox="0 0 10 12"><path d="M0 0L10 6L0 12Z" fill="#14204f"/></svg></div>
  </div>
</footer>
<p class="copyright">Copyright © 2026 Korelith. All Rights Reserved.</p>

</body>
</html>
```